Southport Billboard for Hiring more CDL drivers

I need a catch design for a bill board (size 10ft by 36 ft) to catch the attention for semi truck drivers.
In the design I want it to include:
-My company logo along with my website(brisklanefreighters.com) and my number(503-217-6095) for contact info.
-I also need it to say earn up to $90,000 a year
-I will send a few photos to choose from
-I need the logo to look clean and simple! I don't want it to be cluttered just clean, simple and catchy.!

Target Market(s)

CDL Class A holders
Semi Truck Drivers

Industry/Entity Type

Trucking Company

Font styles to use
Other font styles liked:
• a font to match my logo

Requirements
Must have
• "Make up to $90,000"
"brisklanefreighters.com"
"503-217-6095"

```html
<!DOCTYPE html>
<html lang="en">
<head>
<meta charset="utf-8">
<title>Brisk Lane Freighters – Driver Hiring Billboard</title>
<link rel="stylesheet" href="https://fonts.googleapis.com/css2?family=Barlow:wght@700;800&family=Barlow+Condensed:wght@700;800&display=swap">
<style>
  :root {
    --ink: #22251f;
    --paper: #f2f2f0;
    --paper-shade: #d9dad6;
    --white: #ffffff;
    --stage: #e6e7e3;
    --photo-sky: #e9ecee;
    --photo-truck: #8e9f8c;
    --photo-ground: #6f6c66;
  }
  html, body {
    margin: 0;
    width: 1200px;
    height: 706px;
    overflow: hidden;
    background: var(--stage);
  }
  .billboard {
    position: absolute;
    left: 40px;
    top: 196px;
    width: 1030px;
    height: 288px;
    transform: scale(1.0874);
    transform-origin: top left;
    background: var(--ink);
    overflow: hidden;
    font-family: "Barlow", sans-serif;
  }
  .light-field {
    position: absolute;
    inset: 0;
  }
  .truck-photo {
    position: absolute;
    left: 585px;
    top: 0;
    width: 445px;
    height: 288px;
    background:
      linear-gradient(180deg, transparent 60%, var(--photo-ground) 100%),
      radial-gradient(ellipse 60% 45% at 45% 60%, var(--photo-truck) 0%, rgba(142,159,140,0) 100%),
      linear-gradient(180deg, var(--photo-sky), #cfd3d4);
  }
  .corner-mark {
    position: absolute;
    right: 35px;
    top: 0;
    width: 62px;
    height: 70px;
  }
  .corner-mark .back { position: absolute; left: 0; top: 0; width: 40px; height: 48px; background: var(--paper-shade); }
  .corner-mark .front { position: absolute; right: 0; top: 0; width: 42px; height: 70px; background: var(--ink); }
  .brand-name {
    position: absolute;
    left: 22px;
    top: 26px;
    width: 230px;
    margin: 0;
    font-family: "Barlow Condensed", sans-serif;
    font-weight: 800;
    color: var(--white);
    font-size: 52px;
    line-height: 0.95;
    text-transform: uppercase;
    letter-spacing: 1px;
  }
  .pay-offer {
    position: absolute;
    left: 320px;
    top: 43px;
    width: 265px;
    height: 92px;
    background: var(--ink);
  }
  .tag {
    position: absolute;
    background: var(--white);
    color: var(--ink);
    font-family: "Barlow Condensed", sans-serif;
    font-weight: 700;
    font-size: 23px;
    line-height: 1;
    padding: 3px 10px;
    border: 3px solid var(--ink);
    text-transform: uppercase;
    white-space: nowrap;
  }
  .tag-earn { left: 34px; top: -15px; }
  .tag-year { right: 8px; bottom: -27px; }
  .pay-amount {
    position: absolute;
    left: 0;
    right: 0;
    top: 18px;
    text-align: center;
    color: var(--white);
    font-weight: 800;
    font-size: 58px;
    line-height: 1;
  }
  .website {
    position: absolute;
    left: 275px;
    top: 180px;
    width: 320px;
    height: 32px;
    background: var(--ink);
    color: var(--white);
    font-weight: 700;
    font-size: 18px;
    line-height: 32px;
    text-align: center;
    text-transform: uppercase;
    letter-spacing: 0.5px;
  }
  .phone {
    position: absolute;
    left: 40px;
    top: 222px;
    color: var(--white);
    font-weight: 800;
    font-size: 56px;
    line-height: 1;
    letter-spacing: 4px;
  }
</style>
</head>
<body>
  <section class="billboard" aria-label="Brisk Lane Freighters hiring billboard">
    <svg class="light-field" width="1030" height="288" viewBox="0 0 1030 288" aria-hidden="true">
      <defs>
        <linearGradient id="paperFade" x1="0" y1="0" x2="1" y2="0">
          <stop offset="0" stop-color="#f7f7f5"/>
          <stop offset="1" stop-color="#dcdddb"/>
        </linearGradient>
      </defs>
      <polygon fill="url(#paperFade)"
        points="248,0 1030,0 1030,220 268,220 262,205 276,190 258,172 270,150 252,128 266,104 250,80 262,56 248,30"/>
    </svg>
    <div class="truck-photo" role="img" aria-label="Photo of a green semi truck hauling white cargo vans on a car-carrier trailer"></div>
    <div class="corner-mark" aria-hidden="true"><span class="back"></span><span class="front"></span></div>

    <h1 class="brand-name">Brisk Lane Freighters</h1>

    <div class="pay-offer">
      <span class="tag tag-earn">Earn up to</span>
      <div class="pay-amount">$90,000</div>
      <span class="tag tag-year">A year</span>
    </div>

    <div class="website">brisklanefreighters.com</div>
    <div class="phone">503-217-6095</div>
  </section>
</body>
</html>
```